依頼詳細
RPE歯科クリニック~行きます訪問歯科・送迎歯科~
のパンフレットを作成依頼致します。

1.パンフレットに使用したいデータ等がございません。以前使用していたパンフレットをPDFで添付いたしますのでご確認ください。添付エクセルデータがございます。こちらを参考にA4両面に収めてレイアウトしてください。

2. パンフレットは以前のパンフレットの(ピンク×水色、ピンク、水色)を希望しております。

3.1枚目の車のロゴはないので、作成いただいてもフリー素材でも結構ですのでお願い致します。

4.MAPは、添付フィル≪MAP_image≫をご確認ください。

5.仕上がりはA4両面イラストレーターデザインを希望いたします。フルカラーでお願いします。
サイズ
A4
ページ数
4ページ
希望イメージ
シンプル 複雑
単色 カラフル
暗い 明るい
日常 高級
遊び心 厳粛
未来的 伝統的
女性的 男性的
希望する色
赤系、水色系
納品ファイル
• イラストレーター形式 (.ai)
補足説明
修正致します

1.添付エクセルデータがございます。→PDFデータの為、文字おこしお願い致します。
医院名
RPE歯科クリニック
~行きます訪問歯科・送迎歯科~
パンフレットのカテゴリになっておりますが、
A4サイズ両面のチラシ作成依頼になります。

よろしくお願いいたします。
コンペ当選者を確約に変更いたしましたのでよろしくお願いいたします。

色使いや、歯を使ったイラストの可愛さと、全体的に見やすくバランスが良かったです。

たくさんのご提案ありがとうございました。 慣れない依頼にご提案くださり感謝しています。 また、機会がありましたら是非ご協力ください。 ありがとうございました。

```html
<!DOCTYPE html>
<html lang="ja">
<head>
<meta charset="UTF-8">
<title>RPE歯科クリニック 訪問歯科・送迎歯科</title>
<link href="https://fonts.googleapis.com/css2?family=M+PLUS+Rounded+1c:wght@500;700;800&family=Noto+Sans+JP:wght@400;500;700&display=swap" rel="stylesheet">
<style>
:root{
  --teal:#5cb6c6;
  --sky:#72c3da;
  --sky-light:#e6f4f8;
  --pink:#ee7c9c;
  --pink-light:#f9d6e0;
  --ink:#4a4a4a;
  --paper:#ffffff;
}
*{margin:0;padding:0;box-sizing:border-box}
html,body{width:858px;height:1200px;overflow:hidden;background:var(--paper)}
body{font-family:"Noto Sans JP",sans-serif;color:var(--ink);position:relative}
.flyer{position:relative;width:858px;height:1200px;padding:0 48px}
.clinic-name{
  font-family:"M PLUS Rounded 1c",sans-serif;font-weight:800;
  color:var(--teal);font-size:52px;letter-spacing:4px;text-align:center;
  padding-top:28px;line-height:1.2;display:flex;justify-content:center;align-items:center;gap:14px
}
.clinic-name .dot{width:18px;height:18px;border-radius:50%;background:var(--teal);display:inline-block}
.tagline{
  font-family:"M PLUS Rounded 1c",sans-serif;font-weight:700;
  color:var(--teal);font-size:36px;text-align:center;letter-spacing:3px;margin-top:6px
}
.hero{
  margin:18px -48px 0;height:290px;
  background:linear-gradient(180deg,#ffffff 0%,#eef7f0 35%,#d5ebd9 70%,#c7dfc9 100%);
}
.section-title{
  display:flex;align-items:center;justify-content:center;gap:14px;
  font-family:"M PLUS Rounded 1c",sans-serif;font-weight:800;font-size:28px;letter-spacing:2px
}
.section-title::before,.section-title::after{content:"";flex:0 0 200px;height:2px;background:currentColor;opacity:.5}
.about .section-title{color:var(--sky);margin-top:16px}
.about p{font-size:19px;line-height:1.75;text-align:center;margin-top:10px}
.treatments .section-title{color:var(--pink);margin-top:14px}
.tiles{display:grid;grid-template-columns:repeat(4,1fr);gap:16px;margin-top:14px}
.tile{
  background:var(--pink);border-radius:6px;height:170px;
  display:flex;flex-direction:column;align-items:center;justify-content:center;gap:12px;
  color:#fff;font-weight:700;font-size:17px;text-align:center;line-height:1.35
}
.tile .icon{width:70px;height:70px;border-radius:50%;background:#f6b4c7}
.flow-band{
  margin-top:22px;background:var(--sky);color:#fff;
  font-family:"M PLUS Rounded 1c",sans-serif;font-weight:800;font-size:26px;
  text-align:center;padding:6px 0;letter-spacing:2px
}
.steps{list-style:none;margin-top:8px}
.step{display:flex;align-items:center;border-bottom:1px solid #cfe8ef;min-height:56px;position:relative}
.step-name{flex:0 0 220px;color:var(--sky);font-weight:700;font-size:22px;padding-left:8px}
.step-text{flex:1;font-size:15px;line-height:1.5;border-left:2px solid var(--sky-light);padding:6px 0 6px 14px}
.arrow{position:absolute;left:18px;bottom:-12px;width:18px;height:12px;z-index:1}
</style>
</head>
<body>
<main class="flyer">
  <header>
    <h1 class="clinic-name"><span>RPE</span><span class="dot"></span><span>歯科クリニック</span></h1>
    <p class="tagline">〜行きます訪問歯科・送迎歯科〜</p>
  </header>

  <div class="hero" role="img" aria-label="クリニックの送迎車と木々、公園のベンチのイラスト"></div>

  <section class="about">
    <h2 class="section-title">訪問歯科診療とは</h2>
    <p>介護施設やご自宅で寝たきりの方や歩行が困難で通院できない方<br>のもとへ、歯科医師や歯科衛生士が訪問し、診療を行うサービスです。</p>
  </section>

  <section class="treatments">
    <h2 class="section-title">治療内容</h2>
    <div class="tiles">
      <div class="tile"><span class="icon" role="img" aria-label="歯のアイコン"></span>虫歯・歯周病<br>の治療、予防</div>
      <div class="tile"><span class="icon" role="img" aria-label="入れ歯のアイコン"></span>入れ歯の作成、<br>修理、調整</div>
      <div class="tile"><span class="icon" role="img" aria-label="歯科器具のアイコン"></span>口腔ケアで<br>感染症予防</div>
      <div class="tile"><span class="icon" role="img" aria-label="口元のアイコン"></span>お口のリハビリ</div>
    </div>
  </section>

  <section class="flow">
    <h2 class="flow-band">訪問診療の流れ</h2>
    <ol class="steps">
      <li class="step"><span class="step-name">1. お申し込み</span><span class="step-text">お電話・FAXなどでお気軽にお申し込みください。</span>
        <svg class="arrow" viewBox="0 0 18 12"><path d="M0 0h18L9 12z" fill="#72c3da"/></svg></li>
      <li class="step"><span class="step-name">2. 訪問日の調整</span><span class="step-text">ご希望に合わせて訪問日を決定します。</span>
        <svg class="arrow" viewBox="0 0 18 12"><path d="M0 0h18L9 12z" fill="#72c3da"/></svg></li>
      <li class="step"><span class="step-name">3. 無料検診</span><span class="step-text">お口の状態を診察します。費用は一切かかりません。</span>
        <svg class="arrow" viewBox="0 0 18 12"><path d="M0 0h18L9 12z" fill="#72c3da"/></svg></li>
      <li class="step"><span class="step-name">4. 治療</span><span class="step-text">訪問治療を開始します。初診時・月初は、<br>各種保険証が必要になります。1日の診療時間は30分程度です。</span>
        <svg class="arrow" viewBox="0 0 18 12"><path d="M0 0h18L9 12z" fill="#72c3da"/></svg></li>
      <li class="step"><span class="step-name">5. 今後のご相談</span><span class="step-text">定期検診やブラッシング等のアフターケアのために<br>定期的にお伺いします。定期検診の結果により治療を再開します。</span></li>
    </ol>
  </section>
</main>
</body>
</html>
```